Property Development company needs a business card design

i need a business card design for my company. we are a very small property developer specialising in land subdivisions in geelong Australia.

I would like to see a splash of brown yellow brown that is my favorite football team colors. (Pelmury) Its needs to be not offensive and slighlty subtle or mysterious or cheeky. I would like a white background with black writing.

Company is Varnel Property Developments. We dont have a logo - maybe a picture of a house /fence / gate / road could or couldnt work? I dont really know.

```html
<!DOCTYPE html>
<html lang="en">
<head>
<meta charset="utf-8">
<title>Varnel Property Developments – Business Card</title>
<link rel="stylesheet" href="https://fonts.googleapis.com/css2?family=Carlito&family=Arimo&display=swap">
<style>
  :root {
    --brown: #613b2d;
    --yellow: #efc132;
    --paper-light: #ffffff;
    --paper-shade: #e9eaea;
    --text-grey: #5a5a5a;
    --icon-grey: #d3d3d3;
  }
  * { margin: 0; padding: 0; box-sizing: border-box; }
  html, body { width: 1200px; height: 741px; overflow: hidden; }
  .card {
    position: relative;
    width: 1200px;
    height: 741px;
    overflow: hidden;
    background: radial-gradient(ellipse at 30% 45%, var(--paper-light) 0%, #f5f5f5 55%, var(--paper-shade) 100%);
  }
  .card-shapes { position: absolute; inset: 0; width: 1200px; height: 741px; }
  .company-name {
    position: absolute;
    left: 148px;
    top: 104px;
    font-family: "Carlito", "Calibri", sans-serif;
    font-size: 55px;
    font-weight: 400;
    line-height: 1;
    color: var(--brown);
    letter-spacing: -0.3px;
    white-space: nowrap;
  }
  .contact {
    position: absolute;
    font-family: "Arimo", Arial, sans-serif;
    font-size: 28px;
    line-height: 1;
    color: var(--text-grey);
    white-space: nowrap;
  }
  .contact-phone { left: 97px; top: 486px; }
  .contact-email { left: 43px; top: 569px; }
  .contact-web { left: 45px; top: 616px; }
  .phone-icon { position: absolute; left: 43px; top: 482px; width: 40px; height: 30px; }
</style>
</head>
<body>
  <div class="card">
    <svg class="card-shapes" viewBox="0 0 1200 741" aria-hidden="true">
      <!-- top-left accent bars -->
      <rect class="accent-bar-brown" x="44" y="0" width="10" height="176" fill="var(--brown)"/>
      <rect class="accent-bar-yellow" x="62" y="0" width="58" height="158" fill="var(--yellow)"/>
      <!-- bottom-right diagonal stripes -->
      <polygon class="stripe-thin" points="640,741 1200,300 1200,326 673,741" fill="var(--brown)"/>
      <polygon class="stripe-yellow" points="720,741 1200,362 1200,446 826,741" fill="var(--yellow)"/>
      <polygon class="corner-brown" points="870,741 1200,481 1200,741" fill="var(--brown)"/>
    </svg>

    <h1 class="company-name">Varnel Property Developments</h1>

    <svg class="phone-icon" viewBox="0 0 40 30" aria-hidden="true">
      <rect x="0" y="6" width="36" height="22" rx="3" fill="var(--icon-grey)"/>
      <path d="M2 10 q16 -10 32 0 v4 h-8 v-3 h-16 v3 h-8 z" fill="#fff" opacity="0.9"/>
      <circle cx="18" cy="20" r="5" fill="#fff"/>
      <circle cx="18" cy="20" r="2.5" fill="var(--icon-grey)"/>
    </svg>

    <p class="contact contact-phone">+1 4820 55317</p>
    <p class="contact contact-email">Email@northmeadstudio.com</p>
    <p class="contact contact-web">northmeadstudio.com</p>
  </div>
</body>
</html>
```